CAMBRAI CELEBRATES ANDOUILETTE

On the occasion of the big annual sale, in CAMBRAI, the 24th celebrates the Cambrai specialty "andouillette de CAMBRAI".

On this occasion, we are developing a special menu for this day;

- Authentic CAMBRAI sausage, old-fashioned mustard sauce, served with fresh fries cooked in beef fat and green salad
- CAMBRAI andouillette salad (lettuce, tomatoes, onions, CAMBRAI andouillette, Tome de VERLANNE, Cambrai apples
- Andouillette gratin (Homemade mash, CAMBRAI andouillette, old-fashioned mustard, gratin with VERLANNE tome
- BRUSCHETTA: Cream base, CAMBRAI sausage, VERLANNE tome, onions, old-fashioned mustard
- Grilled ham
- Fried mussels, with VERLANNE tome cream

The event will take place on Sunday July 2, in continuous service.

Please write in French, and insert the logo of the establishment of 57 and illustrate well.

THANKS

```html
<!DOCTYPE html>
<html lang="fr">
<head>
<meta charset="utf-8">
<title>Andouillette de Cambrai – Le 57</title>
<link rel="stylesheet" href="https://fonts.googleapis.com/css2?family=Poppins:wght@400;500;600;700&family=Montserrat:wght@800&family=Libre+Baskerville:wght@400;700&family=Oswald:wght@500;700&display=swap">
<style>
  :root {
    --page: #eceef0;
    --ink: #1b1b1b;
    --dark: #2b2c2e;
    --gold: #d6a527;
    --gold-text: #e3a92f;
    --orange: #d4881c;
    --white: #ffffff;
    --paper-top: #f7f7f7;
    --paper-mid: #e4e4e4;
  }
  * { margin: 0; padding: 0; box-sizing: border-box; }
  html, body { width: 1200px; height: 2540px; overflow: hidden; background: var(--page); }
  .flyer {
    position: absolute; left: 58px; top: 501px;
    width: 903px; height: 1282px;
    transform: scale(1.2); transform-origin: top left;
    overflow: hidden;
    box-shadow: 0 10px 30px rgba(0,0,0,.18);
    font-family: "Poppins", sans-serif;
  }
  .flyer__backdrop {
    position: absolute; inset: 0;
    background: radial-gradient(ellipse at 50% 30%, var(--paper-top) 0%, var(--paper-mid) 100%);
  }
  .flyer__bands { position: absolute; inset: 0; }
  .abs { position: absolute; line-height: 1; white-space: nowrap; }
  .occasion {
    left: 0; width: 903px; text-align: center; top: 52px;
    font-size: 22px; letter-spacing: 7px; font-weight: 500; color: var(--ink);
  }
  .brand-mark {
    left: 396px; top: 87px; width: 124px; height: 124px;
    border: 2px solid var(--ink); border-radius: 50%;
  }
  .brand-name {
    left: 396px; top: 87px; width: 124px; height: 124px;
    display: flex; align-items: center; justify-content: center;
    font-size: 34px; font-weight: 600; color: var(--ink);
  }
  .kicker {
    left: 0; width: 903px; text-align: center; top: 223px;
    font-size: 27px; letter-spacing: 2.5px; color: var(--ink);
  }
  .title-line {
    left: 0; width: 903px; text-align: center; top: 258px;
    font-family: "Libre Baskerville", serif; font-size: 56px; color: var(--ink);
  }
  .title-main {
    left: 0; width: 903px; text-align: center; top: 310px;
    font-family: "Libre Baskerville", serif; font-weight: 700; font-size: 82px; color: var(--gold);
  }
  .photo {
    position: absolute; border-radius: 50%;
    border: 8px solid var(--white);
    box-shadow: 0 0 0 3px rgba(255,255,255,.35);
  }
  .photo--salad { left: 573px; top: 392px; width: 270px; height: 270px;
    background: radial-gradient(circle at 45% 60%, #f2efe6 0%, #8fbf5a 38%, #6c9a8e 70%, #4e3226 100%); }
  .photo--bruschetta { left: 563px; top: 707px; width: 280px; height: 280px;
    background: radial-gradient(circle at 50% 45%, #ee7a45 0%, #d9a476 40%, #b27b4d 70%, #f3f1ee 100%); }
  .menu-heading {
    left: 59px; top: 500px;
    font-family: "Montserrat", sans-serif; font-weight: 800; font-size: 47px; color: var(--white);
  }
  .menu { position: absolute; left: 0; top: 0; }
  .dish__title {
    position: absolute; left: 82px; width: 423px;
    font-size: 23px; font-weight: 700; color: var(--gold-text); line-height: 1;
    padding-bottom: 6px; border-bottom: 2px solid var(--gold-text);
  }
  .dish__bullet {
    position: absolute; left: 52px; width: 12px; height: 12px; border-radius: 50%; background: var(--gold-text);
  }
  .dish__desc {
    position: absolute; left: 82px; width: 420px;
    font-size: 16px; line-height: 19px; color: var(--white);
  }
  .follow {
    left: 51px; top: 1150px; font-size: 27px; color: var(--gold-text);
  }
  .social-dot {
    position: absolute; left: 52px; top: 1194px; width: 38px; height: 38px; border-radius: 50%; background: #3b5aa0;
  }
  .handle { left: 103px; top: 1202px; font-size: 24px; color: var(--white); }
  .date-day {
    left: 538px; top: 1028px;
    font-family: "Oswald", sans-serif; font-weight: 700; font-size: 160px; color: var(--orange); line-height: .8;
  }
  .date-text {
    left: 628px; top: 1037px;
    font-family: "Oswald", sans-serif; font-weight: 500; font-size: 64px; line-height: 62px;
    color: var(--white); letter-spacing: -1px; transform: scaleX(.82); transform-origin: left top;
  }
</style>
</head>
<body>
<main class="flyer">
  <div class="flyer__backdrop" role="img" aria-label="Photo en fond clair d'une table dressée avec assiette"></div>
  <svg class="flyer__bands" viewBox="0 0 903 1282" width="903" height="1282" aria-hidden="true">
    <path d="M0,352 Q451,520 903,357 L903,1282 L0,1282 Z" fill="var(--gold)"/>
    <path d="M0,398 Q451,548 903,380 L903,1282 L0,1282 Z" fill="var(--dark)"/>
  </svg>

  <p class="abs occasion">A L'OCCASION DE LA GRANDE VENTE ANNUELLE</p>
  <div class="abs brand-mark"></div>
  <div class="abs brand-name">Le 57</div>
  <p class="abs kicker">FÊTE LA SPÉCIALITÉ DE CAMBRAI</p>
  <h1 class="abs title-line">ANDOUILLETTE DE</h1>
  <p class="abs title-main">CAMBRAI</p>

  <div class="photo photo--salad" role="img" aria-label="Photo d'une salade composée à l'andouillette dans une assiette"></div>
  <div class="photo photo--bruschetta" role="img" aria-label="Photo de bruschettas garnies de crème et de tomates"></div>

  <h2 class="abs menu-heading">MENUS SPÉCIAUX</h2>
  <section class="menu">
    <span class="dish__bullet" style="top:570px"></span>
    <h3 class="dish__title" style="top:566px">SAUCISSE CAMBRAI AUTHENTIQUE</h3>
    <p class="dish__desc" style="top:606px">Sauce moutarde à l'ancienne, servie avec frites fraîches cuites dans la graisse de boeuf et salade verte</p>

    <span class="dish__bullet" style="top:688px"></span>
    <h3 class="dish__title" style="top:684px">CAMBRAI ANDOUILLETTE SALAD</h3>
    <p class="dish__desc" style="top:724px">lettuce, tomatoes, onions, CAMBRAI andouillette, Tome de VERLANNE, Cambrai apples</p>

    <span class="dish__bullet" style="top:786px"></span>
    <h3 class="dish__title" style="top:782px">ANDOUILLETTE GRATINÉE</h3>
    <p class="dish__desc" style="top:831px">Purée maison, andouillette CAMBRAI, moutarde à l'ancienne, gratinée à la tome VERLANNE</p>

    <span class="dish__bullet" style="top:895px"></span>
    <h3 class="dish__title" style="top:891px">BRUSCHETTA</h3>
    <p class="dish__desc" style="top:943px">Base crème, saucisse CAMBRAI, tome VERLANNE, oignons, moutarde à l'ancienne</p>

    <span class="dish__bullet" style="top:1003px"></span>
    <h3 class="dish__title" style="top:999px">JAMBON GRILLÉ</h3>

    <span class="dish__bullet" style="top:1058px"></span>
    <h3 class="dish__title" style="top:1054px">MOULES POÊLÉES</h3>
    <p class="dish__desc" style="top:1095px">crème de tome VERLANNE</p>
  </section>

  <p class="abs follow">follow us on</p>
  <span class="social-dot"></span>
  <p class="abs handle">@lebar57</p>

  <p class="abs date-day">2</p>
  <p class="abs date-text">JUILLET<br>DIMANCHE</p>
</main>
</body>
</html>
```